A boutique/architectural website for a landscape company

I'm after a minimilstic boutique website for my landscape design and construction business. I have been exploring Wix and created some pages on that but want something more aesthetic.

Industry/Entity Type

Landscaping design and construction

Number of Pages Required

5+ page

Font styles to use
Sans Serif

Colors

Designer to choose colors to be used in the design.

Requirements
Must have
• an architectural, minimalistic look
Nice to have
• Simplicitly and nice images
Should not have
• A corporate look

```html
<!DOCTYPE html>
<html lang="en">
<head>
<meta charset="utf-8">
<title>Verdale Landscaping + Design</title>
<link rel="stylesheet" href="https://fonts.googleapis.com/css2?family=Montserrat:wght@400;500;600;700;800&display=swap">
<style>
:root{
  --teal:#0f6a5b;
  --teal-dark:#0b5447;
  --teal-soft:#1f7a69;
  --ink:#2b2b2b;
  --muted:#6f6f6f;
  --paper:#ffffff;
  --mist:#eeeeee;
  --mist-dark:#e2e2e2;
  --line:#bdbdbd;
}
*{box-sizing:border-box;margin:0;padding:0}
html,body{width:1200px;height:3817px;overflow:hidden}
body{position:relative;font-family:"Montserrat",sans-serif;color:var(--ink);background:var(--paper)}
.abs{position:absolute}
.btn{position:absolute;display:flex;align-items:center;justify-content:center;border-radius:22px;font-size:15px;letter-spacing:.2px;text-transform:uppercase}
.btn-teal{background:var(--teal);color:#fff}
.btn-dark{background:#333;color:#fff}
.btn-white{background:#fff;color:var(--teal)}

/* Hero */
.hero{left:0;top:0;width:1200px;height:712px;
  background:linear-gradient(180deg,#1d2b1a 0%,#3d5a2a 30%,#4f8a2c 55%,#5b9a2e 75%,#3f6f22 100%)}
.hero-shade{left:0;top:0;width:1200px;height:712px;background:linear-gradient(90deg,rgba(0,0,0,.35),rgba(0,0,0,0) 60%)}
.brand{color:#fff;font-weight:500;letter-spacing:2px}
.brand-mark{left:228px;top:40px;width:34px;height:34px;border:2px solid #fff;border-radius:50%}
.brand-name{left:193px;top:92px;width:104px;text-align:center;font-size:17px}
.brand-tag{left:188px;top:114px;width:114px;text-align:center;font-size:7px;letter-spacing:.8px}
.call{left:835px;top:22px;color:#fff;font-size:12px}
.call b{font-size:16px;font-weight:700}
.nav{top:70px;color:#fff;font-size:15px;font-weight:500}
.nav.active{color:#3fc4a4;border-bottom:2px solid #3fc4a4;padding-bottom:2px}
.quote{left:921px;top:65px;width:116px;height:28px;font-size:13px;text-transform:none}
.hero-title{left:193px;top:284px;color:#fff;font-size:48px;font-weight:800;letter-spacing:-.5px}
.hero-sub{left:193px;top:346px;color:#fff;font-size:46px;font-weight:500}
.hero-btn{left:193px;top:434px;width:195px;height:44px}
.arrow{top:345px;width:42px;height:42px;border-radius:50%;display:flex;align-items:center;justify-content:center}
.arrow-l{left:69px;background:rgba(255,255,255,.4)}
.arrow-r{left:1089px;background:#fff}

/* Services */
.services-bg{left:0;top:700px;width:1200px;height:562px;background:linear-gradient(180deg,#f4f4f4,#fff 40%,#fafafa)}
.svc-photo{width:200px;height:200px;border-radius:50%;border:6px solid #fff;box-shadow:0 2px 10px rgba(0,0,0,.18)}
.svc-title{width:300px;text-align:center;font-size:18px;font-weight:500;letter-spacing:.5px}
.svc-text{width:240px;text-align:center;font-size:11.5px;line-height:19px;color:var(--muted)}
.svc-cta{left:514px;top:1130px;width:172px;height:40px}

/* About */
.about{left:0;top:1262px;width:1200px;height:574px;background:linear-gradient(90deg,#0e6456,#13705f 60%,#0f6a5b)}
.about h2{position:absolute;left:194px;top:1344px;color:#fff;font-size:31px;font-weight:400}
.about-p{left:194px;width:560px;color:#fff;font-size:12px;line-height:20.5px}
.feat-icon{top:1596px;width:44px;height:44px}
.feat-title{top:1655px;color:#fff;font-size:13.5px;font-weight:600}
.feat-text{top:1681px;width:180px;color:#fff;font-size:11.5px;line-height:17.5px}
.about-person{left:800px;top:1340px;width:326px;height:496px;border-radius:160px 160px 0 0;
  background:linear-gradient(180deg,#e9c98a 0%,#f1d7bf 30%,#2f8f3e 60%,#237a33 100%)}

/* Works */
.works h2{position:absolute;left:0;top:1952px;width:1200px;text-align:center;font-size:33px;font-weight:400;letter-spacing:.5px}
.works h2 b{color:var(--teal);font-weight:800}
.works-sub{left:0;top:2003px;width:1200px;text-align:center;font-size:14px;color:#555}
.works-mark{left:588px;top:1890px;width:24px;height:24px;border-radius:50%;background:var(--teal)}
.tile{position:absolute}
.tile-overlay{background:rgba(15,106,91,.82);display:flex;flex-direction:column;align-items:center;justify-content:center;color:#fff;font-size:15px}
.tile-overlay .dot{width:40px;height:40px;border-radius:50%;background:#fff;margin-bottom:14px;display:flex;align-items:center;justify-content:center}
.learn{left:524px;top:2590px;width:152px;height:37px}

/* Process */
.process{left:0;top:2696px;width:1200px;height:460px;background:var(--mist)}
.eyebrow{left:228px;top:2778px;font-size:12px;color:var(--teal);font-weight:500}
.process h3{position:absolute;left:228px;top:2804px;font-size:26px;font-weight:700;line-height:34px;width:330px}
.process-text{left:228px;top:2922px;width:300px;font-size:11px;line-height:19px}
.step-icon{left:601px;width:42px;height:38px;background:#3a3a3a;display:flex;align-items:center;justify-content:center}
.step-no{left:659px;font-size:11px}
.step-name{left:659px;font-size:18px;font-weight:700}
.step-line{left:659px;width:307px;height:1px;background:#9a9a9a}
.step-toggle{left:946px;font-size:22px;font-weight:300;line-height:1}
.step-text{left:659px;top:2838px;width:300px;font-size:10px;line-height:16px}

/* CTA */
.cta-title{left:0;top:3226px;width:1200px;text-align:center;color:#fff;font-size:30px;font-weight:800;letter-spacing:-.3px}
.cta-sub{left:0;top:3270px;width:1200px;text-align:center;color:#fff;font-size:30px;font-weight:400}
.cta-btn{left:514px;top:3341px;width:172px;height:37px}

/* Footer */
.footer{left:0;top:3481px;width:1200px;height:267px;background:var(--mist)}
.foot-bar{left:0;top:3748px;width:1200px;height:69px;background:var(--mist-dark)}
.foot-mark{left:243px;top:3555px;width:28px;height:28px;border-radius:50%;background:var(--teal)}
.foot-name{left:194px;top:3620px;width:126px;text-align:center;color:var(--teal);font-size:16px;letter-spacing:2px}
.foot-tag{left:194px;top:3641px;width:126px;text-align:center;color:var(--teal);font-size:7px;letter-spacing:.8px}
.foot-btn{left:194px;top:3667px;width:144px;height:32px;font-size:12px}
.vrule{top:3530px;width:1px;height:170px;background:#cfcfcf}
.foot-h{font-size:15px;color:var(--teal);font-weight:500}
.foot-h::before{content:"";position:absolute;left:0;top:-18px;width:30px;height:2px;background:var(--teal)}
.foot-link{left:436px;font-size:11px}
.contact-row{left:593px;font-size:11px;line-height:17px;display:flex;gap:8px}
.contact-row svg{flex:none;margin-top:1px}
.social{top:3585px;width:22px;height:22px;border-radius:50%;background:var(--teal)}
.news-input{left:861px;top:3686px;width:117px;height:27px;background:#fff;font-size:10px;color:#888;padding:8px 10px}
.news-send{left:978px;top:3686px;width:29px;height:27px;background:var(--teal);display:flex;align-items:center;justify-content:center}
.copy{top:3776px;font-size:11px;color:#777}
</style>
</head>
<body>

<!-- Hero -->
<div class="abs hero" role="img" aria-label="Landscaped garden with stone steps, lawn and stepping stones"></div>
<div class="abs hero-shade"></div>

<div class="abs brand brand-mark"></div>
<div class="abs brand brand-name">VERDALE</div>
<div class="abs brand brand-tag">LANDSCAPING + DESIGN</div>

<div class="abs call">CALL US NOW: <b>01 234 5678 9</b></div>
<div class="abs nav active" style="left:464px">Home</div>
<div class="abs nav" style="left:532px">About Us</div>
<div class="abs nav" style="left:624px">Services</div>
<div class="abs nav" style="left:711px">Our Works</div>
<div class="abs nav" style="left:810px">Contact Us</div>
<div class="btn btn-teal quote">Get A Quote</div>

<div class="abs hero-title">MAKE YOUR LAWN</div>
<div class="abs hero-sub">Clean &amp; Beautiful</div>
<div class="btn btn-teal hero-btn">Contact us now</div>

<div class="abs arrow arrow-l"><svg width="14" height="14" viewBox="0 0 14 14"><path d="M9 2 4 7l5 5" fill="none" stroke="#333" stroke-width="2"/></svg></div>
<div class="abs arrow arrow-r"><svg width="14" height="14" viewBox="0 0 14 14"><path d="M5 2l5 5-5 5" fill="none" stroke="#333" stroke-width="2"/></svg></div>

<svg class="abs" style="left:586px;top:578px" width="28" height="44" viewBox="0 0 28 44">
  <rect x="6" y="2" width="16" height="24" rx="8" fill="none" stroke="#fff" stroke-width="1.5"/>
  <line x1="14" y1="8" x2="14" y2="13" stroke="#fff" stroke-width="1.5"/>
  <path d="M14 28v12M10 36l4 4 4-4" fill="none" stroke="#fff" stroke-width="1.5"/>
</svg>

<!-- Services -->
<div class="abs services-bg"></div>
<svg class="abs" style="left:0;top:650px" width="1200" height="70" viewBox="0 0 1200 70">
  <polygon points="0,58 600,12 1200,58 1200,70 0,70" fill="#f4f4f4"/>
  <polyline points="0,58 600,12 1200,58" fill="none" stroke="#0c3d22" stroke-width="3"/>
</svg>

<div class="abs svc-photo" style="left:205px;top:780px;background:linear-gradient(135deg,#5f9c3b,#c9c6bd 50%,#e08a3a 75%,#5a8c32)" role="img" aria-label="Stepping stones with flowering plants"></div>
<div class="abs svc-photo" style="left:500px;top:747px;background:linear-gradient(180deg,#a9b6c4,#e9dcc2 50%,#bba27f)" role="img" aria-label="Fenced courtyard with outdoor seating"></div>
<div class="abs svc-photo" style="left:792px;top:780px;background:linear-gradient(180deg,#3d5a2c,#6a8a3a 40%,#5aa12f 70%,#4d8c2a)" role="img" aria-label="Paved path across green lawn"></div>

<div class="abs svc-title" style="left:155px;top:1004px">LANDSCAPING</div>
<div class="abs svc-title" style="left:450px;top:973px;color:var(--teal)">FENCING</div>
<div class="abs svc-title" style="left:742px;top:1004px">PAVING</div>

<p class="abs svc-text" style="left:185px;top:1034px">Lorem ipsum dolor sit amet, consectetur adipiscing elit. Mauris in rhoncus orci. Pellentesque ac consequat nulla.</p>
<p class="abs svc-text" style="left:480px;top:1003px">Lorem ipsum dolor sit amet, consectetur adipiscing elit. Mauris in rhoncus orci. Pellentesque ac consequat nulla.</p>
<p class="abs svc-text" style="left:772px;top:1034px">Lorem ipsum dolor sit amet, consectetur adipiscing elit. Mauris in rhoncus orci. Pellentesque ac consequat nulla.</p>

<div class="btn btn-dark svc-cta">Contact us now</div>

<!-- About -->
<section class="abs about">
</section>
<div class="about"><h2>ABOUT <b style="font-weight:800">VERDALE</b></h2></div>
<p class="abs about-p" style="top:1399px">Lorem ipsum dolor sit amet, consectetur adipiscing elit. Mauris in rhoncus orci. Pellentesque ac consequat nulla. Sed facilisis accumsan dui nec elementum. Maecenas posuere porttitor mauris eu vestibulum. In consequat facilisis urna.</p>
<p class="abs about-p" style="top:1474px">Quis varius mauris commodo non. Donec condimentum porttitor enim, in varius velit blandit gravida. Phasellus id mauris vel sapien mollis convallis. Mauris eget leo imperdiet, posuere quam ac, lobortis libero. Nullam et urna sed lorem interdum interdum. Suspendisse luctus eros risus, non pharetra tellus finibus id.</p>

<svg class="abs feat-icon" style="left:194px" viewBox="0 0 44 44" fill="none" stroke="#fff" stroke-width="2.5">
  <path d="M3 8h6l6 16h20l4-12H12"/><circle cx="18" cy="34" r="5"/><path d="M30 24l6 14"/>
</svg>
<svg class="abs feat-icon" style="left:403px" viewBox="0 0 44 44" fill="none" stroke="#fff" stroke-width="3">
  <circle cx="22" cy="22" r="18"/><path d="M14 22l6 6 11-12"/>
</svg>
<svg class="abs feat-icon" style="left:613px" viewBox="0 0 44 44" fill="none" stroke="#fff" stroke-width="2.5">
  <circle cx="22" cy="12" r="6"/><path d="M22 18v10M10 28h24M12 33h20M14 38h16"/>
</svg>

<div class="abs feat-title" style="left:194px">EXCELLENT SERVICES</div>
<div class="abs feat-title" style="left:403px">GUARANTEED WORK</div>
<div class="abs feat-title" style="left:613px">QUALITY &amp; RELIABLITY</div>
<p class="abs feat-text" style="left:194px">Lorem ipsum dolor sit amet elit- Mauris in rhoncus orci nulla Sed facilisis accumsan dui.</p>
<p class="abs feat-text" style="left:403px">Lorem ipsum dolor sit amet elit- Mauris in rhoncus orci nulla Sed facilisis accumsan dui.</p>
<p class="abs feat-text" style="left:613px">Lorem ipsum dolor sit amet elit- Mauris in rhoncus orci nulla Sed facilisis accumsan dui.</p>

<div class="abs about-person" role="img" aria-label="Smiling gardener in green apron holding a potted plant and trowel"></div>

<!-- Latest works -->
<section class="works">
  <div class="abs works-mark"></div>
  <h2>LATEST <b>WORKS</b></h2>
</section>
<div class="abs works-sub">Lorem ipsum dolor sit amet, consectetur adipiscing elit. Mauris in rhoncus orci.</div>

<div class="tile" style="left:194px;top:2056px;width:400px;height:237px;background:linear-gradient(180deg,#3c5a33,#8a8a7c 40%,#5aa02e 70%,#4d8f27)" role="img" aria-label="Terraced garden with stone wall and timber steps"></div>
<div class="tile" style="left:603px;top:2056px;width:401px;height:237px;background:linear-gradient(135deg,#4e8b2f,#b9b9b2 45%,#e07a2e 70%,#5e9430)" role="img" aria-label="Stepping stones with orange flowers"></div>
<div class="tile tile-overlay" style="left:194px;top:2304px;width:264px;height:237px" role="img" aria-label="Courtyard with outdoor chairs">
  <div class="dot"><svg width="14" height="14" viewBox="0 0 14 14" fill="none" stroke="#0f6a5b" stroke-width="1.6"><path d="M6 2H2v10h10V8M8 2h4v4M12 2 6 8"/></svg></div>
  VIEW MORE
</div>
<div class="tile" style="left:468px;top:2304px;width:264px;height:237px;background:linear-gradient(135deg,#5a4a3e,#8a3d2c 35%,#3d4c5c 60%,#b07a3a)" role="img" aria-label="Crazy-paving flagstone path"></div>
<div class="tile" style="left:741px;top:2304px;width:263px;height:237px;background:linear-gradient(180deg,#6a8a5a,#8aa06a 40%,#5aa02e 70%,#4a8a26)" role="img" aria-label="Garden with gabion wall and lawn"></div>

<div class="btn btn-dark learn">Learn more</div>

<!-- Process -->
<section class="abs process"></section>
<div class="abs eyebrow">OUR PROCESS</div>
<div class="process"><h3>A COMPANY YOU CAN TRUST TO BE WITH YOU AT EVERY STEP</h3></div>
<p class="abs process-text">We don't sub-contract any of our work out and only have one job running at a time. This means the quality of every job is at its maximum leavel and your job has our full attention.</p>

<div class="abs step-icon" style="top:2786px"><svg width="20" height="20" viewBox="0 0 20 20" fill="none" stroke="#fff" stroke-width="1.5"><path d="M3 17l3-1 10-10-2-2L4 14zM12 6l2 2"/></svg></div>
<div class="abs step-no" style="top:2786px">STEP 1</div>
<div class="abs step-name" style="top:2798px">CONTACT</div>
<div class="abs step-toggle" style="top:2794px;font-size:18px">✕</div>
<div class="abs step-line" style="top:2820px"></div>
<p class="abs step-text">Fill out our contact form or give us a call to beging your FREE service estimate. Lorem Ipsum is simply dummy text of the printing and typesetting industry. Lorem Ipsum has been the industry's standard dummy text ever since the 1500s.</p>

<div class="abs step-icon" style="top:2930px"><svg width="16" height="20" viewBox="0 0 16 20" fill="none" stroke="#fff" stroke-width="1.5"><path d="M2 1h8l4 4v14H2zM5 9h6M5 12h6M5 15h6"/></svg></div>
<div class="abs step-no" style="top:2931px">STEP 2</div>
<div class="abs step-name" style="top:2943px">PROPOSAL</div>
<div class="abs step-toggle" style="top:2940px">+</div>
<div class="abs step-line" style="top:2966px"></div>

<div class="abs step-icon" style="top:2985px"><svg width="20" height="20" viewBox="0 0 20 20" fill="none" stroke="#fff" stroke-width="1.5"><path d="M2 18h16M4 18V9l6-5 6 5v9M8 18v-5h4v5"/></svg></div>
<div class="abs step-no" style="top:2986px">STEP3</div>
<div class="abs step-name" style="top:2998px">CONSTRUCTION</div>
<div class="abs step-toggle" style="top:2995px">+</div>
<div class="abs step-line" style="top:3021px"></div>

<!-- CTA band -->
<svg class="abs" style="left:0;top:3100px" width="1200" height="381" viewBox="0 0 1200 381" role="img" aria-label="Garden backdrop in deep green">
  <defs><linearGradient id="ctaFill" x1="0" y1="0" x2="0" y2="1"><stop offset="0" stop-color="#136f5f"/><stop offset="1" stop-color="#0c5a4c"/></linearGradient></defs>
  <polygon points="0,44 600,4 1200,32 1200,381 0,381" fill="url(#ctaFill)"/>
  <polyline points="0,44 600,4 1200,32" fill="none" stroke="#1f8a76" stroke-width="5"/>
</svg>
<div class="abs cta-title">WE TAKE CARE OF YOUR LANDSCAPE.</div>
<div class="abs cta-sub">YOU TAKE BACK YOUR FREE TIME.</div>
<div class="btn btn-white cta-btn">Contact us now</div>

<!-- Footer -->
<footer class="abs footer"></footer>
<div class="abs foot-mark"></div>
<div class="abs foot-name">VERDALE</div>
<div class="abs foot-tag">LANDSCAPING + DESIGN</div>
<div class="btn btn-teal foot-btn">Contact us now</div>

<div class="abs vrule" style="left:382px"></div>
<div class="abs vrule" style="left:550px"></div>
<div class="abs vrule" style="left:804px"></div>

<div class="abs foot-h" style="left:436px;top:3550px">Site Links</div>
<div class="abs foot-link" style="top:3593px">Home</div>
<div class="abs foot-link" style="top:3614px">About Us</div>
<div class="abs foot-link" style="top:3636px">Services</div>
<div class="abs foot-link" style="top:3657px">Our Work</div>
<div class="abs foot-link" style="top:3679px">Contact Us</div>

<div class="abs foot-h" style="left:593px;top:3550px">Contact Us</div>
<div class="abs contact-row" style="top:3592px"><svg width="14" height="14" viewBox="0 0 14 14" fill="none" stroke="#0f6a5b" stroke-width="1.3"><path d="M3 1l2 3-1.5 1.5a7 7 0 0 0 5 5L10 9l3 2-1 2C6 13 1 8 1 2z"/></svg>Phone: 234 567 89012</div>
<div class="abs contact-row" style="top:3624px;width:190px"><svg width="14" height="14" viewBox="0 0 14 14" fill="none" stroke="#0f6a5b" stroke-width="1.3"><path d="M7 13s-4-4.5-4-8a4 4 0 0 1 8 0c0 3.5-4 8-4 8z"/><circle cx="7" cy="5" r="1.5"/></svg><span>Address: 48 Fernbrook Lane, Suite 9, Greenfield, Gf</span></div>
<div class="abs contact-row" style="top:3684px"><svg width="14" height="14" viewBox="0 0 14 14" fill="none" stroke="#0f6a5b" stroke-width="1.3"><rect x="1" y="3" width="12" height="8"/><path d="M1 3l6 5 6-5"/></svg>Email: hello@verdale-studio.com</div>

<div class="abs foot-h" style="left:861px;top:3550px">Get Connected</div>
<div class="abs social" style="left:861px"></div>
<div class="abs social" style="left:887px"></div>
<div class="abs social" style="left:913px"></div>

<div class="abs foot-h" style="left:861px;top:3652px">Newsletter</div>
<div class="abs news-input">Email...</div>
<div class="abs news-send"><svg width="14" height="14" viewBox="0 0 14 14" fill="#fff"><path d="M1 7 13 1 9 13 7 8z"/></svg></div>

<div class="abs foot-bar"></div>
<div class="abs copy" style="left:194px">@2021 Verdale Landscaping &nbsp;|&nbsp; All Rights Reserved.</div>
<div class="abs copy" style="left:815px">Terms &amp; Conditions &nbsp;|&nbsp; Privacy Policy</div>

</body>
</html>
```